UPDATED BRIEF: Hypermobile EDS Book Cover Contest

I am writing a print book. I need cover designs to evaluate with your creativity. It is a nonfiction memoir meets self-help guide to living with a rare, incurable chronic illness called EDS. See attached Word doc for book details and copy. It is designed to be an inspiration story of living well with this disease so mindset is a key theme. I'm looking for all types of ideas including photography (sailboat, mountain, journey concepts), type flat designs highlighting hypermobility (a key part of the disease), including good use of color and white space. I want it to be legible, intriguing, and emotive if possible. I need someone to be able to produce and provide the production files and/or edit the final text back copy as it is not yet final. I will be sharing the contest with my fan base. I will ultimately need the cover, back cover, spine, and audio and ebook covers done all the same just reformatted to size. Print book 6x9 to be done first. I dont want to provide too much direction so you can be creative.
Updates

I uploaded a new brief for updated author name and back cover. Please update and I will start the poll. I will also extend the project timeline.

Can anyone create a design with the typeset words of hypermobile on the title being "pinched" by a string? Like holding it all together by a string?

Went on vacation/holiday

Target Market(s)

chronic illness disease victims, specifically those with Hypermobile Ehlers Danlos Syndrome (EDS), dysautonomia (POTS) or craniocervical instability in the neck

Industry/Entity Type

Self help, personal development, memoir

Font styles to use
Sans Serif

Colors
FFC000
F8CF3A
FAE287
FDF2CF
FEFAEE

Requirements
Must have
• legible, intriguing even emotive design with text or photos
Nice to have
• Potentially visually showing a journey, hypermobility, or overcoming obstacles
Should not have
• black dark backgrounds

```html
<!DOCTYPE html>
<html lang="en">
<head>
<meta charset="utf-8">
<title>Keeping It All Steady When You're Overflexible — Book Cover</title>
<link href="https://fonts.googleapis.com/css2?family=Oswald:wght@500;600;700&family=Mulish:wght@600&display=swap" rel="stylesheet">
<style>
  :root {
    --sky-top: #5f86b3;
    --sky-mid: #a9b9cf;
    --glow: #fff6e4;
    --sunset: #f3b06e;
    --haze: #e9c2b0;
    --ridge: #8e8fa6;
    --hill: #7f9a5c;
    --hill-dark: #4f6a3a;
    --title-ink: #111111;
    --title-red: #d9141b;
    --band: #ffc000;
    --band-ink: #0d0d0d;
  }
  * { margin: 0; padding: 0; box-sizing: border-box; }
  html, body {
    width: 800px;
    height: 1200px;
    overflow: hidden;
    background: #ffffff;
  }
  .cover {
    position: relative;
    width: 800px;
    height: 1200px;
    overflow: hidden;
  }
  .cover-scene {
    position: absolute;
    inset: 0 0 138px 0;
    background:
      radial-gradient(ellipse 420px 260px at 52% 36%, var(--glow) 0%, rgba(255,240,215,0.85) 35%, rgba(255,230,200,0) 75%),
      linear-gradient(180deg,
        var(--sky-top) 0%,
        var(--sky-mid) 14%,
        #f1d9c3 30%,
        var(--sunset) 44%,
        #f6cdb0 52%,
        var(--haze) 58%,
        var(--ridge) 63%,
        #9aa08a 70%,
        var(--hill) 80%,
        var(--hill-dark) 100%);
  }
  .cover-title {
    position: absolute;
    left: 0;
    top: 0;
    width: 800px;
    height: 560px;
  }
  .title-lead {
    font-family: 'Oswald', sans-serif;
    font-weight: 600;
    font-size: 60px;
    fill: var(--title-ink);
  }
  .title-key {
    font-family: 'Oswald', sans-serif;
    font-weight: 700;
    font-size: 212px;
    fill: var(--title-red);
  }
  .cover-subtitle {
    position: absolute;
    left: 0;
    top: 474px;
    width: 800px;
    text-align: center;
    font-family: 'Mulish', sans-serif;
    font-weight: 600;
    font-size: 26px;
    line-height: 37px;
    color: var(--title-ink);
  }
  .author-band {
    position: absolute;
    left: 0;
    bottom: 0;
    width: 800px;
    height: 138px;
    background: var(--band);
  }
  .author-band svg {
    display: block;
    width: 800px;
    height: 138px;
  }
  .author-name {
    font-family: 'Oswald', sans-serif;
    font-weight: 700;
    font-size: 100px;
    fill: var(--band-ink);
  }
</style>
</head>
<body>
  <main class="cover">
    <div class="cover-scene" role="img" aria-label="Photograph of a fenced dirt path climbing a grassy mountain ridge toward a glowing sunset sky, with distant hills and a lake"></div>

    <svg class="cover-title" viewBox="0 0 800 560" xmlns="http://www.w3.org/2000/svg" aria-label="Keeping It All Steady When You're Overflexible">
      <text class="title-lead" x="400" y="206" text-anchor="middle" textLength="384" lengthAdjust="spacingAndGlyphs">KEEPING IT ALL</text>
      <text class="title-lead" x="400" y="265" text-anchor="middle" textLength="610" lengthAdjust="spacingAndGlyphs">STEADY WHEN YOU’RE</text>
      <text class="title-key" x="36" y="455" textLength="707" lengthAdjust="spacingAndGlyphs">OVERFLEXIBLE</text>
    </svg>

    <p class="cover-subtitle">Build a Calmer Everyday Life<br>with Loose Joints, Dizziness, and Pain</p>

    <footer class="author-band">
      <svg viewBox="0 0 800 138" xmlns="http://www.w3.org/2000/svg" aria-label="Dana R. Wells">
        <text class="author-name" x="49" y="110" textLength="702" lengthAdjust="spacingAndGlyphs">DANA R. WELLS</text>
      </svg>
    </footer>
  </main>
</body>
</html>
```